CD-/Plattencover für Musikalbum
Zielgruppe
Wir sind eine Tonträgerfirma und bewegen uns im Low-Budget-Segment.
Aufgabenstellung
Artwork-Design (Cover) für ein Musikalbum : „Sommerpfauenfest”
Wir benötigen nicht das komplette Artwork, sondern ein Frontcover
(121 x 120 mm + 20 mm Beschnitt) wg. etwaiger Verschiebung der Positionierung.
Fertigstellung (Aufziehen des Inlays und Labels) erfolgt später bei uns im Hause.
Wir benötigen später eine offene psd-Datei mit allen Ebenen.
Wichtig: Schriften nicht gerastert ggfs. Schrift mitliefern.
Was wir uns vorstellen:
- Entsprechend der Musik Bild, Tracks Beispiele:
Bis zum letzten Leuchtturm
Eine Rose, die nach Morgen duftet
Ganz viel Sonnenschein
Der Sommer bleibt Gold
Egon, wir tanzen bis Mainz
- Bildmaterial sollte bei pixelkammer, bildarena oder o-frame ausgesucht werden, das Bildmaterial wird dann später auch von uns dort eingekauft.
- keine Künstlerfotos.

```html
<!DOCTYPE html>
<html lang="de">
<head>
<meta charset="utf-8">
<title>Sommerpfauenfest – Frontcover</title>
<link rel="stylesheet" href="https://fonts.googleapis.com/css2?family=Great+Vibes&family=Open+Sans:wght@700;800&family=Raleway:wght@300&display=swap">
<style>
  :root {
    --navy-deep: #0a2138;
    --navy: #0f3a5e;
    --blue-glow: #1a8fd6;
    --blue-bright: #38b4f0;
    --ink: #050505;
    --paper: #ffffff;
    --lemon: #d8d634;
  }
  html, body {
    margin: 0;
    padding: 0;
    width: 1200px;
    height: 1192px;
    overflow: hidden;
    background: var(--navy-deep);
  }
  .cover {
    display: block;
    width: 1200px;
    height: 1192px;
  }
  .volume-number {
    font-family: "Open Sans", Arial, sans-serif;
    font-weight: 800;
    font-size: 36px;
    fill: var(--paper);
  }
  .track-title {
    font-family: "Open Sans", Arial, sans-serif;
    font-weight: 800;
    font-size: 21px;
    fill: var(--paper);
    text-anchor: middle;
    letter-spacing: 0.3px;
  }
  .title-script {
    font-family: "Great Vibes", cursive;
    font-size: 178px;
    fill: var(--paper);
    text-anchor: middle;
  }
  .title-caps {
    font-family: "Raleway", Arial, sans-serif;
    font-weight: 300;
    font-size: 50px;
    fill: var(--paper);
    text-anchor: middle;
    letter-spacing: 12px;
  }
  .feature-track {
    font-family: "Open Sans", Arial, sans-serif;
    font-weight: 800;
    font-size: 18px;
    fill: var(--ink);
    text-anchor: middle;
  }
</style>
</head>
<body>
<svg class="cover" viewBox="0 0 1200 1192" xmlns="http://www.w3.org/2000/svg">
  <defs>
    <radialGradient id="bg-glow" cx="50%" cy="50%" r="62%">
      <stop offset="0" stop-color="var(--blue-bright)"/>
      <stop offset="0.28" stop-color="var(--blue-glow)"/>
      <stop offset="0.62" stop-color="var(--navy)"/>
      <stop offset="1" stop-color="var(--navy-deep)"/>
    </radialGradient>
    <linearGradient id="spark-top" x1="0" y1="0" x2="0" y2="1">
      <stop offset="0" stop-color="#ffffff" stop-opacity="0"/>
      <stop offset="0.5" stop-color="#ffffff" stop-opacity="0.95"/>
      <stop offset="1" stop-color="#ffffff" stop-opacity="0.2"/>
    </linearGradient>
    <linearGradient id="spark-bottom" x1="0" y1="1" x2="0" y2="0">
      <stop offset="0" stop-color="#ffffff" stop-opacity="0"/>
      <stop offset="0.5" stop-color="#ffffff" stop-opacity="0.95"/>
      <stop offset="1" stop-color="#ffffff" stop-opacity="0.2"/>
    </linearGradient>
    <filter id="soft-shadow" x="-20%" y="-20%" width="140%" height="140%">
      <feDropShadow dx="0" dy="4" stdDeviation="8" flood-color="#000" flood-opacity="0.45"/>
    </filter>
    <clipPath id="title-diamond-clip">
      <polygon points="600,236 974,610 600,984 226,610"/>
    </clipPath>
  </defs>

  <!-- background -->
  <rect class="backdrop" role="img" aria-label="Dunkelblauer Hintergrund mit feinem Ornamentmuster und hellblauem Lichtschein in der Mitte" x="0" y="0" width="1200" height="1192" fill="url(#bg-glow)"/>

  <text class="volume-number" x="22" y="60">27</text>

  <!-- track diamonds -->
  <g class="track-diamond" filter="url(#soft-shadow)">
    <polygon points="296,170 456,330 296,490 136,330" fill="var(--ink)"/>
    <polygon points="296,168 336,208 296,248 256,208" fill="url(#spark-top)"/>
  </g>
  <text class="track-title" x="296" y="300">
    <tspan x="296">EINE ROSE,</tspan>
    <tspan x="296" dy="26">DIE NACH</tspan>
    <tspan x="296" dy="26">MORGEN</tspan>
    <tspan x="296" dy="26">DUFTET</tspan>
  </text>

  <g class="track-diamond" filter="url(#soft-shadow)">
    <polygon points="906,170 1066,330 906,490 746,330" fill="var(--ink)"/>
    <polygon points="906,168 946,208 906,248 866,208" fill="url(#spark-top)"/>
  </g>
  <text class="track-title" x="906" y="318">
    <tspan x="906">BIS ZUM LETZTEN</tspan>
    <tspan x="906" dy="26">LEUCHTTURM</tspan>
  </text>

  <g class="track-diamond" filter="url(#soft-shadow)">
    <polygon points="296,750 456,910 296,1070 136,910" fill="var(--ink)"/>
    <polygon points="296,992 336,1032 296,1072 256,1032" fill="url(#spark-bottom)"/>
  </g>
  <text class="track-title" x="296" y="902">
    <tspan x="296">GANZ VIEL</tspan>
    <tspan x="296" dy="26">SONNENSCHEIN</tspan>
  </text>

  <g class="track-diamond" filter="url(#soft-shadow)">
    <polygon points="906,750 1066,910 906,1070 746,910" fill="var(--ink)"/>
    <polygon points="906,992 946,1032 906,1072 866,1032" fill="url(#spark-bottom)"/>
  </g>
  <text class="track-title" x="906" y="890">
    <tspan x="906">EGON, WIR</tspan>
    <tspan x="906" dy="26">TANZEN BIS</tspan>
    <tspan x="906" dy="26">MAINZ*</tspan>
  </text>

  <!-- title diamond -->
  <g class="title-diamond" filter="url(#soft-shadow)">
    <polygon points="600,220 990,610 600,1000 210,610" fill="var(--paper)"/>
    <polygon points="600,236 974,610 600,984 226,610" fill="var(--ink)"/>
    <g clip-path="url(#title-diamond-clip)">
      <rect class="title-band-top" x="200" y="220" width="800" height="206" fill="var(--lemon)"/>
      <rect class="title-band-bottom" x="200" y="794" width="800" height="206" fill="var(--lemon)"/>
    </g>
  </g>

  <text class="title-script" x="600" y="640">Sommer</text>
  <text class="title-caps" x="606" y="718">PFAUENFEST</text>

  <text class="feature-track" x="600" y="832">
    <tspan x="600">DER SOMMER BLEIBT GOLD</tspan>
    <tspan x="600" dy="23">U.V.M.</tspan>
  </text>
</svg>
</body>
</html>
```